Vornel Technologies business card design

We need a business card designed with our new logo. it would be great if the card could communicate it is a technology based company.

Target Market(s)

system integrators

Industry/Entity Type

technology, IOT

Contact Information for Business Card

Name, designation, Address, telephone number, email address

Requirements
Must have
• logo and company name
Nice to have
• something to do with technology

```html
<!DOCTYPE html>
<html lang="en">
<head>
<meta charset="utf-8">
<title>Vornel Technologies – Business Card</title>
<link rel="stylesheet" href="https://fonts.googleapis.com/css2?family=Open+Sans:wght@400;600;700&display=swap">
<style>
  :root {
    --stage: #3a3b3d;
    --card-dark: #323233;
    --card-light: #ffffff;
    --ink: #2b2b2b;
    --orange: #ee8210;
    --rule: #3a3a3a;
  }
  * { box-sizing: border-box; margin: 0; padding: 0; }
  html, body { width: 1200px; height: 801px; overflow: hidden; }
  body {
    background: var(--stage);
    font-family: "Open Sans", Arial, sans-serif;
    position: relative;
  }
  .card {
    position: absolute;
    width: 525px;
    height: 300px;
    border-radius: 14px;
    border-bottom: 3px solid var(--orange);
    box-shadow: 0 10px 24px rgba(0,0,0,.35);
    overflow: hidden;
  }
  .card--back { left: 45px; top: 250px; background: var(--card-dark); }
  .card--front { left: 630px; top: 250px; background: var(--card-light); }

  .brand {
    position: absolute;
    display: flex;
    align-items: center;
    gap: 10px;
    font-weight: 700;
    color: var(--orange);
    letter-spacing: .02em;
    text-transform: uppercase;
    white-space: nowrap;
  }
  .brand__mark { width: 16px; height: 16px; background: var(--orange); flex: none; }
  .card--back .brand { left: 0; right: 0; top: 130px; justify-content: center; font-size: 26px; }
  .card--front .brand { left: 26px; top: 150px; font-size: 18px; gap: 8px; color: var(--ink); }
  .card--front .brand__mark { width: 13px; height: 13px; }

  .divider {
    position: absolute;
    left: 300px; top: 40px;
    width: 2px; height: 150px;
    background: linear-gradient(var(--rule) 0 22%, var(--orange) 22% 78%, var(--rule) 78%);
  }
  .person { position: absolute; left: 320px; top: 48px; }
  .person__name { font-size: 21px; font-weight: 700; color: var(--ink); letter-spacing: -.01em; line-height: 1.1; white-space: nowrap; }
  .person__role { font-size: 14px; color: var(--orange); margin-top: 2px; }

  .contacts { position: absolute; left: 320px; top: 112px; list-style: none; }
  .contacts li { display: flex; align-items: center; gap: 8px; font-size: 13px; color: var(--ink); margin-bottom: 9px; white-space: nowrap; }
  .contacts svg { width: 12px; height: 12px; flex: none; fill: var(--orange); }

  .address {
    position: absolute;
    left: 26px; right: 24px; bottom: 30px;
    font-size: 14px; color: var(--ink);
    text-align: right;
  }
</style>
</head>
<body>
  <section class="card card--back" aria-label="Card back">
    <div class="brand"><span class="brand__mark"></span>Vornel Technologies</div>
  </section>

  <section class="card card--front" aria-label="Card front">
    <div class="brand"><span class="brand__mark"></span>Vornel Technologies</div>
    <div class="divider"></div>
    <div class="person">
      <p class="person__name">DANA WHITLOCK</p>
      <p class="person__role">Founder</p>
    </div>
    <ul class="contacts">
      <li><svg viewBox="0 0 12 12"><path d="M2.5 0.5l2 2.5-1.2 1.4a7 7 0 0 0 4.3 4.3L9 7.5l2.5 2-1.5 2C5 11.5 0.5 7 0.5 2z"/></svg>(310) 555-0148</li>
      <li><svg viewBox="0 0 12 12"><path d="M0 2h12v1.2L6 7 0 3.2z M0 4.6l6 3.8 6-3.8V10H0z"/></svg>info@vornel-tech.com</li>
      <li><svg viewBox="0 0 12 12"><path d="M6 0a6 6 0 1 0 0 12A6 6 0 0 0 6 0zm0 1.6a4.4 4.4 0 1 1 0 8.8 4.4 4.4 0 0 1 0-8.8z"/><rect x="5.2" y="1.5" width="1.6" height="9"/><rect x="1.5" y="5.2" width="9" height="1.6"/></svg>www.vornel-tech.com</li>
    </ul>
    <p class="address">214 Harlan Ridge Rd, Fairview, CA 94590</p>
  </section>
</body>
</html>
```